Very Simple/Minimal Business Card Design Project

The company operates in the industrial maritime infrastructure sector in Brazil. You can find more information on our website www.navortek.com.br WE NEED TO LOOK POWERFUL AND SERIOUS
I have attached a copy of the old cards. We would like something more professional / industrial / sexy that also includes the position.

The card can be double sided or not. We would like you to propose as many options.

Thank you
Updates

Many thanks, do let me know if you have any questions. I am under a lot of time pressure to try and have them printed over the next days or so.

Please could you use the following information

for the address: Rua Tapiraçu, 417 - Centro, Rio de Janeiro, 20034-118, Brasil

for the mobile: +55 21 8237 9412
for the landline: +55 21 4096 3578

and position:  Diretor Geral

Thakn you

Target Market(s)

Shipowners, bankers, industrial companies

Industry/Entity Type

Industrial

Requirements
Must have
• POWERFUL
SERIOUS
SOLID
BIG CORPORATION

```html
<!DOCTYPE html>
<html lang="pt-BR">
<head>
<meta charset="utf-8">
<title>Navortek – Business Card</title>
<link rel="stylesheet" href="https://fonts.googleapis.com/css2?family=Arimo:ital,wght@0,400;0,700;1,400&display=swap">
<style>
  :root {
    --brand-blue: #0000ff;
    --brand-green: #00ff00;
    --accent-cyan: #00ffff;
    --paper: #ffffff;
    --ink: #000000;
    --icon-blue: #2a3be8;
    --icon-green: #4cd62a;
    --icon-cyan: #22d3f0;
    --icon-steel: #3f8fd8;
  }
  * { box-sizing: border-box; margin: 0; padding: 0; }
  html, body { width: 1200px; height: 1000px; overflow: hidden; background: var(--paper); }
  body { position: relative; font-family: "Arimo", Arial, sans-serif; }

  .card { position: absolute; border-radius: 24px; overflow: hidden; }

  .card-front {
    left: 238px; top: 15px; width: 673px; height: 481px;
    background: var(--paper);
    border: 2px solid var(--brand-blue);
  }
  .front-panel {
    position: absolute; left: 0; top: 0; width: 202px; height: 100%;
    background: linear-gradient(to bottom, var(--brand-blue) 88%, #4a55ff 100%);
  }
  .panel-accent {
    position: absolute; left: 0; top: 0; width: 202px; height: 200px;
    background: linear-gradient(135deg, var(--brand-green) 0%, #2bb0a0 45%, #1a2cf0 100%);
    clip-path: polygon(0 0, 202px 0, 202px 60px, 150px 200px, 50px 170px, 0 80px);
    opacity: .9;
  }
  .panel-brand {
    position: absolute; left: 22px; top: 393px;
    display: flex; align-items: center; gap: 8px;
  }
  .brand-square { width: 42px; height: 42px; border-radius: 5px; background: var(--brand-green); }
  .panel-brand .brand-name {
    font-weight: 700; font-size: 20px; color: var(--brand-green); letter-spacing: .5px;
  }

  .holder { position: absolute; left: 202px; width: 469px; top: 80px; text-align: center; }
  .holder-name { font-weight: 700; font-size: 29px; color: var(--ink); letter-spacing: .3px; transform: scaleY(1.08); }
  .holder-role { font-style: italic; font-size: 25px; color: var(--ink); margin-top: 2px; }

  .contact { position: absolute; font-style: italic; color: var(--ink); }
  .contact-icon { position: absolute; width: 38px; height: 38px; }
  .mobile { left: 224px; top: 256px; font-size: 20px; }
  .landline { left: 446px; top: 256px; font-size: 20px; }
  .email { left: 224px; top: 358px; font-size: 16.5px; }
  .address { left: 448px; top: 356px; font-size: 19px; line-height: 24px; }

  .card-back {
    left: 238px; top: 508px; width: 671px; height: 480px;
    background: var(--brand-blue);
  }
  .back-brand {
    position: absolute; left: 101px; top: 132px;
    display: flex; align-items: center; gap: 32px;
  }
  .back-brand .brand-square { width: 104px; height: 104px; border-radius: 10px; }
  .back-brand .brand-name { font-weight: 700; font-size: 56px; color: var(--brand-green); letter-spacing: 1px; }
  .back-url {
    position: absolute; left: 0; width: 100%; top: 372px; text-align: center;
    font-style: italic; font-size: 40px; color: var(--accent-cyan);
  }
</style>
</head>
<body>

<section class="card card-front">
  <div class="front-panel">
    <div class="panel-accent" role="img" aria-label="Decorative green-to-blue brand graphic"></div>
    <div class="panel-brand">
      <span class="brand-square"></span>
      <span class="brand-name">NAVORTEK</span>
    </div>
  </div>

  <div class="holder">
    <div class="holder-name">RAFAEL MOREIRA</div>
    <div class="holder-role">Diretor Geral</div>
  </div>

  <svg class="contact-icon" style="left:290px;top:203px" viewBox="0 0 38 38" aria-hidden="true">
    <rect x="1" y="1" width="36" height="36" rx="6" fill="var(--icon-blue)"/>
    <rect x="13" y="7" width="12" height="23" rx="2" fill="none" stroke="#fff" stroke-width="2"/>
    <circle cx="19" cy="27" r="1.2" fill="#fff"/>
  </svg>
  <div class="contact mobile">+55 21 8237 9412</div>

  <svg class="contact-icon" style="left:522px;top:203px" viewBox="0 0 38 38" aria-hidden="true">
    <rect x="1" y="1" width="36" height="36" rx="6" fill="var(--icon-green)"/>
    <path d="M12 10c2-1 3 0 4 3s0 3-1 4c1 2 3 4 5 5 1-1 2-2 4-1s4 2 3 4-3 3-6 2C15 25 11 20 10 16c-1-3 0-5 2-6z" fill="#fff"/>
  </svg>
  <div class="contact landline">+55 21 4096 3578</div>

  <svg class="contact-icon" style="left:291px;top:306px" viewBox="0 0 38 38" aria-hidden="true">
    <rect x="1" y="1" width="36" height="36" rx="6" fill="var(--icon-cyan)"/>
    <rect x="8" y="12" width="22" height="15" rx="2" fill="#fff"/>
    <path d="M8 13l11 8 11-8" fill="none" stroke="var(--icon-cyan)" stroke-width="2"/>
  </svg>
  <div class="contact email">rafael@navortek.com.br</div>

  <svg class="contact-icon" style="left:523px;top:306px" viewBox="0 0 38 38" aria-hidden="true">
    <rect x="1" y="1" width="36" height="36" rx="6" fill="var(--icon-steel)"/>
    <rect x="11" y="8" width="16" height="24" fill="#cfe6ff"/>
    <g fill="var(--icon-steel)">
      <rect x="13" y="11" width="4" height="3"/><rect x="21" y="11" width="4" height="3"/>
      <rect x="13" y="17" width="4" height="3"/><rect x="21" y="17" width="4" height="3"/>
      <rect x="13" y="23" width="4" height="3"/><rect x="21" y="23" width="4" height="3"/>
    </g>
  </svg>
  <div class="contact address">
    Rua Tapiraçu, 417<br>
    Centro Rio de Janeiro<br>
    20034-118 Brasil
  </div>
</section>

<section class="card card-back">
  <div class="back-brand">
    <span class="brand-square"></span>
    <span class="brand-name">NAVORTEK</span>
  </div>
  <div class="back-url">www.navortek.com.br</div>
</section>

</body>
</html>
```